Business broker needs designs for business card, letterhead and email signature

I require the following items:
- business cards
- letterhead
- email signature

My company is a Business Broker company that specialises in business sales across various industries. The company has branches in four areas and each area has its own logo and website. Initially for the submission I am happy to inspect 1 design and 1 layout for tallowgatedeals but the winner will need to complete a design for each area.

The four areas are:
1. tallowgatedeals
2. pinecrestfuelagent
3. harrowlinkagent
4. bramblegroceragent

I would like one design for each of the above items for each area. In each design, there should be one prominent logo and then the remaining three should also be included, for eg, the letterhead for the tallowgatedeal area would have the tallowgatedeal logo featuring prominently, somewhere at the top perhaps and the logos of the other three areas would be smaller and perhaps at the bottom, down the side, etc.

For the business cards, one prominent logo should feature on one side with the remaining three logos on the reverse.

The overall objective is for each item to look like it belongs to one family . I need all the source files as I may add new industries moving forward.

Target Market(s)

My company targets business minded people looking to increase wealth,. make an investment or migrate to Australia. People who busy and are looking for efficient and professional service in securing their next business venture.

Industry/Entity Type

Business

Font styles to use
Serif
Sans Serif

Requirements
Must have
• I want something professional and corporate looking, not something cartoony or playful. I am happy for you to be creative.

```html
<!DOCTYPE html>
<html lang="en">
<head>
<meta charset="utf-8">
<title>tallowgatedeals – Letterhead</title>
<link rel="stylesheet" href="https://fonts.googleapis.com/css2?family=Roboto+Condensed:wght@400;700&family=Roboto:wght@300;400;500&display=swap">
<style>
  :root {
    --ink: #333c45;
    --body: #5a5f64;
    --brand-red: #c8202f;
    --grocer-green: #5db33a;
    --fuel-teal: #2bb5a8;
    --link-orange: #f5a01a;
    --paper: #ffffff;
  }
  * { margin: 0; padding: 0; box-sizing: border-box; }
  html, body { width: 848px; height: 1200px; overflow: hidden; background: var(--paper); }
  .letterhead { position: relative; width: 848px; height: 1200px; background: var(--paper); }

  .brand { position: absolute; left: 34px; top: 68px; display: flex; align-items: center; gap: 12px; }
  .brand-mark { width: 44px; height: 44px; background: var(--brand-red); }
  .brand-name { font: 700 36px/1 "Roboto Condensed", sans-serif; color: var(--ink); letter-spacing: -0.5px; }

  .sender { position: absolute; left: 31px; top: 157px; width: 170px; color: var(--ink); font-family: "Roboto Condensed", sans-serif; }
  .sender-address { font-size: 15px; line-height: 16px; letter-spacing: 0.3px; }
  .sender-contact { margin-top: 9px; font-size: 11px; line-height: 19.5px; letter-spacing: 0.6px; }
  .sender-corner { position: absolute; left: 0; top: 0; }

  .letter { position: absolute; left: 257px; top: 156px; width: 521px; font-family: "Roboto", sans-serif; color: var(--body); }
  .letter-date, .letter-subject { font-size: 12.7px; line-height: 24px; color: var(--ink); font-weight: 300; }
  .letter-body { margin-top: 20px; }
  .letter-body p { font-size: 12.3px; line-height: 20.4px; font-weight: 300; text-align: justify; margin-bottom: 20.4px; }
  .signoff { margin-top: 4px; color: var(--ink); }
  .signoff-title { font-size: 17px; font-weight: 500; line-height: 23px; }
  .signoff-name { font-size: 17px; font-weight: 300; line-height: 23px; }

  .branches { position: absolute; left: 0; top: 1108px; width: 848px; height: 24px; }
  .branch { position: absolute; display: flex; align-items: center; gap: 6px; }
  .branch-mark { width: 18px; height: 18px; }
  .branch-name { font: 700 15px/1 "Roboto Condensed", sans-serif; color: var(--ink); }
  .branch--grocer { left: 32px; }
  .branch--grocer .branch-mark { background: var(--grocer-green); }
  .branch--fuel { left: 342px; }
  .branch--fuel .branch-mark { background: var(--fuel-teal); }
  .branch--link { left: 670px; }
  .branch--link .branch-mark { background: var(--link-orange); }
</style>
</head>
<body>
<main class="letterhead">
  <header class="brand">
    <span class="brand-mark"></span>
    <span class="brand-name">tallowgatedeals</span>
  </header>

  <aside class="sender">
    <div class="sender-address">Harlow 27 40218<br>P.O Box 3829</div>
    <div class="sender-contact">info@tallowgatedeals.com<br>+000 000 0 000<br>www.tallowgatedeals.com</div>
    <svg class="sender-corner" width="200" height="110" viewBox="0 0 200 110" aria-hidden="true">
      <path d="M159 83 V104 H137" fill="none" stroke="var(--brand-red)" stroke-width="1.2"/>
    </svg>
  </aside>

  <article class="letter">
    <p class="letter-date">June 17, 2015</p>
    <p class="letter-subject">Lorem Lpsum is Simply</p>
    <div class="letter-body">
      <p>Lorem Ipsum is simply dummy text of the printing and typesetting industry. Lorem Ipsum has been the industry's standard dummy text ever since the 1500s, when an unknown printer took a galley of type and scrambled it to make a type specimen book. It has survived not only five centuries, but also the leap into electronic typesetting, remaining essentially unchanged. It was popularised in the 1960s with the release of Letraset sheets containing Lorem Ipsum passages, and more recently with desktop publishing software like Aldus PageMaker including versions of Lorem Ipsum.</p>
      <p>Lorem Ipsum is simply dummy text of the printing and typesetting industry. Lorem Ipsum has been the industry's standard dummy text ever since the 1500s, when an unknown printer took a galley of type and scrambled it to make a type specimen book. It has survived not only five centuries, but also the leap into electronic typesetting, remaining essentially unchanged. It was popularised in the 1960s with the release of Letraset sheets containing Lorem Ipsum passages, and more recently with desktop publishing software like Aldus PageMaker including versions of Lorem Ipsum.Lorem Ipsum is simply dummy text of the printing and typesetting industry. Lorem Ipsum has been the industry's standard dummy text ever since the 1500s, when an unknown printer took a galley of type and scrambled it to make a type specimen book. It has survived not only five centuries, but also the leap into electronic typesetting, remaining essentially unchanged. It was popularised in the 1960s with the release of Letraset sheets containing Lorem Ipsum passages, and more recently with desktop publishing software like Aldus PageMaker including versions of Lorem Ipsum.</p>
    </div>
    <div class="signoff">
      <p class="signoff-title">Lorem Lpsum is Simply</p>
      <p class="signoff-name">Lorem Ipsum</p>
    </div>
  </article>

  <footer class="branches">
    <div class="branch branch--grocer"><span class="branch-mark"></span><span class="branch-name">bramblegroceragent</span></div>
    <div class="branch branch--fuel"><span class="branch-mark"></span><span class="branch-name">pinecrestfuelagent</span></div>
    <div class="branch branch--link"><span class="branch-mark"></span><span class="branch-name">harrowlinkagent</span></div>
  </footer>
</main>
</body>
</html>
```